Email Banner for Technology Company

We need a new email banner. The purpose of the email banner is to make us look more professional as a business and keep all communications with clients uniform. The previous designs which we have included below have now become outdated as our brand has developed and we need the new banner to become more aligned and modern.
We are a marketing organization that specialises in lead generation, email newsletters are sent to prospects on a regular basis. Therefore, it is important that we have an aesthetically pleasing banner as this is the first real impression prospects have our business. First impressions matter.
We are looking for a new email banner design as the current design is now outdated and does not reflect who we are as a business.
The new banners are required for launch at the start of Q2.
There is future work in the pipeline for the winning design. We have multiple industry sites that will require the new design as well as creating each of these in multiple languages.
The design must include the Lumenfield Dossiers wording the tagline 'The Innovation Lead’s Study Desk'.
It needs to be creative and fun but still remain professional, sticking with the colour theme that already exists.

```html
<!DOCTYPE html>
<html lang="en">
<head>
<meta charset="utf-8">
<title>Lumenfield Dossiers – Email Banners</title>
<link rel="stylesheet" href="https://fonts.googleapis.com/css2?family=Montserrat:wght@700&family=Noto+Sans:wght@500&display=swap">
<style>
  :root {
    --stage: #616161;
    --paper: #ffffff;
    --ink: #0a0a0a;
    --navy: #111a2b;
    --brand-blue: #0096d6;
    --blue-deep: #1f6fd6;
    --blue-mid: #2f8fe4;
    --blue-light: #55d6ff;
    --mist: #e6e6e6;
    --mist-dark: #c9c9c9;
  }
  * { box-sizing: border-box; margin: 0; padding: 0; }
  html, body { width: 1200px; height: 960px; overflow: hidden; background: var(--stage); }
  .stage { position: relative; width: 1200px; height: 960px; }

  .banner { position: absolute; overflow: hidden; background: var(--paper); }
  .banner--wide { left: 48px; top: 122px; width: 1104px; height: 317px; }
  .banner--stacked { left: 45px; top: 500px; width: 1112px; height: 310px; }

  .banner__art { position: absolute; inset: 0; width: 100%; height: 100%; }

  .wordmark {
    position: absolute;
    font-family: "Montserrat", Arial, sans-serif; font-weight: 700;
    color: var(--ink); letter-spacing: -1.5px; white-space: nowrap;
    font-size: 76px; line-height: 92px;
  }
  .banner--wide .wordmark { left: 38px; top: 56px; }
  .banner--stacked .wordmark { left: 37px; top: 34px; }

  .tagline {
    position: absolute; font-family: "Noto Sans", "Segoe UI", sans-serif;
    font-weight: 500; color: var(--ink); white-space: nowrap;
  }
  .banner--wide .tagline { left: 169px; top: 178px; font-size: 38px; line-height: 56px; }
  .banner--stacked .tagline { left: 40px; top: 160px; font-size: 35px; line-height: 46px; }

  .icon-row { position: absolute; display: flex; color: var(--navy); }
  .icon-row svg { fill: currentColor; }
  .banner--wide .icon-row { left: 65px; top: 264px; gap: 8px; }
  .banner--wide .icon-row svg { width: 28px; height: 26px; }
  .banner--stacked .icon-row { left: 878px; top: 230px; gap: 12px; }
  .banner--stacked .icon-row svg { width: 36px; height: 34px; }
</style>
</head>
<body>
<svg width="0" height="0" style="position:absolute" aria-hidden="true">
  <defs>
    <symbol id="icon-database" viewBox="0 0 24 24">
      <ellipse cx="12" cy="5" rx="9" ry="3.2"/>
      <path d="M3 7.5c0 1.8 4 3.2 9 3.2s9-1.4 9-3.2V11c0 1.8-4 3.2-9 3.2S3 12.8 3 11z"/>
      <path d="M3 13.5c0 1.8 4 3.2 9 3.2s9-1.4 9-3.2V17c0 1.8-4 3.2-9 3.2S3 18.8 3 17z"/>
    </symbol>
    <symbol id="icon-group" viewBox="0 0 24 24">
      <circle cx="6" cy="7" r="2.6"/><circle cx="18" cy="7" r="2.6"/><circle cx="12" cy="8" r="3.2"/>
      <path d="M1.5 16c0-2.6 2-4.3 4.5-4.3 1 0 1.8.2 2.5.7-1 1-1.6 2.3-1.6 3.6z"/>
      <path d="M22.5 16c0-2.6-2-4.3-4.5-4.3-1 0-1.8.2-2.5.7 1 1 1.6 2.3 1.6 3.6z"/>
      <path d="M6.5 20c0-3.5 2.4-6 5.5-6s5.5 2.5 5.5 6z"/>
    </symbol>
    <symbol id="icon-user-remove" viewBox="0 0 24 24">
      <circle cx="9" cy="7" r="4"/>
      <path d="M1 21c0-4.3 3.5-7.5 8-7.5s8 3.2 8 7.5z"/>
      <path d="M17.2 9.8l1.6-1.6 1.6 1.6 1.6-1.6 1 1-1.6 1.6 1.6 1.6-1 1-1.6-1.6-1.6 1.6-1-1 1.6-1.6-1.6-1.6z"/>
    </symbol>
    <symbol id="icon-user-check" viewBox="0 0 24 24">
      <circle cx="9" cy="7" r="4"/>
      <path d="M1 21c0-4.3 3.5-7.5 8-7.5s8 3.2 8 7.5z"/>
      <path d="M15.5 11.5l1.3-1.3 1.8 1.8 4.2-4.2 1.3 1.3-5.5 5.5z"/>
    </symbol>
  </defs>
</svg>

<main class="stage">

  <section class="banner banner--wide">
    <svg class="banner__art" viewBox="0 0 1984 569" preserveAspectRatio="none">
      <defs>
        <linearGradient id="wide-mist" x1="0" x2="1" y1="0" y2="0">
          <stop offset="0" stop-color="#f4f4f4"/>
          <stop offset="0.35" stop-color="#dcdcdc"/>
          <stop offset="0.7" stop-color="#ebebeb"/>
          <stop offset="1" stop-color="#f6f6f6"/>
        </linearGradient>
        <linearGradient id="wide-blue" x1="0" x2="1" y1="0.2" y2="0.8">
          <stop offset="0" stop-color="#1f78dc"/>
          <stop offset="0.55" stop-color="#2fa6ee"/>
          <stop offset="1" stop-color="#5ad9ff"/>
        </linearGradient>
        <linearGradient id="wide-stripe" x1="0" x2="0" y1="0" y2="1">
          <stop offset="0" stop-color="#3fb2ee"/>
          <stop offset="1" stop-color="#1d62cc"/>
        </linearGradient>
      </defs>
      <rect width="1984" height="569" fill="url(#wide-mist)" role="img" aria-label="Soft-focus office interior backdrop"/>
      <polygon points="900,0 1290,0 1680,569 1040,569 820,300" fill="#dedede"/>
      <polygon points="1160,0 1410,0 1130,300 1380,569 1130,569 860,300" fill="#f2f2f2"/>
      <polygon points="1084,0 1164,0 864,300 1124,569 1044,569 794,300" fill="url(#wide-stripe)"/>
      <polygon points="1164,0 1230,0 930,300 1190,569 1124,569 864,300" fill="#ffffff"/>
      <polygon points="1674,0 1984,0 1984,569 1659,569 1339,302" fill="url(#wide-blue)" role="img" aria-label="Blue panel with dotted globe and hexagon mesh texture"/>
      <polygon points="232,318 1790,318 1725,430 230,430" fill="rgba(255,255,255,0.55)"/>
    </svg>

    <div class="wordmark">Lumenfield Dossiers</div>
    <p class="tagline">“The Innovation Lead’s Study Desk”</p>
    <div class="icon-row">
      <svg><use href="#icon-database"/></svg>
      <svg><use href="#icon-group"/></svg>
      <svg><use href="#icon-user-remove"/></svg>
      <svg><use href="#icon-user-check"/></svg>
    </div>
  </section>

  <section class="banner banner--stacked">
    <svg class="banner__art" viewBox="0 0 1998 556" preserveAspectRatio="none">
      <defs>
        <linearGradient id="stack-mist" x1="0" x2="1" y1="0" y2="0">
          <stop offset="0" stop-color="#ffffff"/>
          <stop offset="0.25" stop-color="#e4e4e4"/>
          <stop offset="0.6" stop-color="#d2d2d2"/>
          <stop offset="1" stop-color="#eeeeee"/>
        </linearGradient>
        <linearGradient id="stack-blue" x1="0" x2="1" y1="1" y2="0">
          <stop offset="0" stop-color="#1e6ad2"/>
          <stop offset="1" stop-color="#47b6f0"/>
        </linearGradient>
        <linearGradient id="stack-glow" x1="0" x2="1" y1="0" y2="0">
          <stop offset="0" stop-color="#ffffff" stop-opacity="0"/>
          <stop offset="0.5" stop-color="#9fd6f5"/>
          <stop offset="1" stop-color="#2f8ee4"/>
        </linearGradient>
        <linearGradient id="stack-mesh" x1="0" x2="0" y1="0" y2="1">
          <stop offset="0" stop-color="#ffffff"/>
          <stop offset="1" stop-color="#e4e4e4"/>
        </linearGradient>
      </defs>
      <rect width="1998" height="556" fill="#ffffff"/>
      <rect x="1330" y="0" width="668" height="556" fill="url(#stack-mist)" role="img" aria-label="Soft-focus office interior with dotted globe texture"/>
      <polygon points="0,320 860,320 560,556 0,556" fill="url(#stack-mesh)" role="img" aria-label="Hexagon mesh texture"/>
      <polygon points="500,0 990,0 1020,35 540,35" fill="var(--navy)"/>
      <polygon points="950,0 1270,0 1550,300 1480,280 1020,35" fill="url(#stack-glow)"/>
      <polygon points="835,280 1305,280 1310,302 1010,556 560,556 860,302" fill="var(--navy)"/>
      <polygon points="1305,280 1480,280 1550,300 1290,556 1010,556 1310,302" fill="url(#stack-blue)"/>
    </svg>

    <div class="wordmark">Lumenfield Dossiers</div>
    <p class="tagline">“The Innovation<br>Lead’s Study Desk”</p>
    <div class="icon-row">
      <svg><use href="#icon-database"/></svg>
      <svg><use href="#icon-group"/></svg>
      <svg><use href="#icon-user-remove"/></svg>
      <svg><use href="#icon-user-check"/></svg>
    </div>
  </section>

</main>
</body>
</html>
```